Pinecrest Haulers ~ A+ Division of Drelvane

Energetic ,different ,exotic ,modern,
never before done, next level buisness card for a trash dumpster company
is for a trash removal construction company ...please have your wildest ideas i dont want a boring basic buisness card i want people to say wow !! And be able to mention you and who designed my card ...i know you take pride in your work i do to ....3 years ago quillwork from brief hive made a logo for me and i still love it .....use his colors and the word vantor DO NOT USE ROOFING AND REMODELING use Pinecrest Haulers ....look at his Logo i Like the [S] LOGO and word Drelvane ....you surprise me and we will do alot more projects with you and or brief hive ....thank you for your hard work and your time i do appreciate all of you and admire your skills designing .....i really do appreciate all of you thank you -todd
Ps Lets make these biz cards special different from many ,unique

Target Market(s)

Construction .....dumpsters trash Trash removal

Industry/Entity Type

Construction

Contact Information for Business Card

Black gold white maybe more colors

Requirements
Must have
• Drelvane ~Pinecrest Haulers division Serving Atlanta and surrounding areas'Chief executive Todd Marlow cell 404 555 0147 Office 404 888 8888Follow us on fb ,instagram .. email Pinecresthaulers-demo.com Hablamos espaƱol
Nice to have
• Black gold white colors like my logo i updated and you can add more if you want ....its a construction / trucking company dumpster Trash company we recycle also
Should not have
• When you look at my logo (Must not have roofing and remodeling )

```html
<!DOCTYPE html>
<html lang="en">
<head>
<meta charset="utf-8">
<title>Drelvane · Pinecrest Haulers Division — Business Card</title>
<link href="https://fonts.googleapis.com/css2?family=Russo+One&family=Roboto:wght@400;500&display=swap" rel="stylesheet">
<style>
  :root {
    --backdrop: #e6e3de;
    --paper: #f3f3f3;
    --ink: #221f20;
    --gold: #e8b90f;
    --gold-light: #f2d010;
    --gold-deep: #d9a516;
    --white: #ffffff;
  }
  * { box-sizing: border-box; margin: 0; padding: 0; }
  html, body { width: 1200px; height: 960px; overflow: hidden; }
  body {
    background: var(--backdrop);
    position: relative;
    font-family: "Roboto", Arial, sans-serif;
  }
  .card {
    position: absolute;
    width: 600px;
    height: 343px;
    box-shadow: 0 3px 6px rgba(0,0,0,0.35);
    overflow: hidden;
  }
  .card-front { left: 314px; top: 113px; background: var(--paper); }
  .card-back {
    left: 311px; top: 472px;
    background: radial-gradient(ellipse at 50% 40%, var(--gold-light) 0%, var(--gold) 50%, var(--gold-deep) 100%);
  }

  /* brand lockup */
  .brand { position: absolute; display: flex; align-items: center; }
  .brand-mark { width: 78px; height: 80px; flex: none; }
  .brand-text { margin-left: 13px; white-space: nowrap; }
  .brand-name {
    font-family: "Russo One", "Arial Black", sans-serif;
    font-size: 38px; line-height: 1;
    letter-spacing: 0.5px;
    color: var(--ink);
  }
  .brand-division {
    font-family: "Russo One", "Arial Black", sans-serif;
    font-size: 11.5px; letter-spacing: 1.2px;
    line-height: 1;
    margin-top: 3px;
    color: var(--gold-deep);
  }
  .card-front .brand { left: 109px; top: 52px; }
  .card-front .brand-mark { background: linear-gradient(135deg, var(--gold-light), var(--gold-deep)); }
  .card-back .brand { left: 138px; top: 137px; }
  .card-back .brand-mark { width: 68px; height: 68px; background: var(--ink); }
  .card-back .brand-text { margin-left: 11px; }
  .card-back .brand-name { font-size: 33px; }
  .card-back .brand-division { color: var(--ink); font-size: 10px; letter-spacing: 1px; }

  /* contact band */
  .contact-band {
    position: absolute; left: 0; top: 187px;
    width: 100%; height: 122px;
    background: var(--ink);
    text-align: center;
    color: var(--white);
  }
  .person-name {
    font-family: "Russo One", "Arial Black", sans-serif;
    font-size: 21px; letter-spacing: 1px; line-height: 1;
    color: var(--gold);
    margin-top: 18px;
  }
  .person-title {
    display: flex; align-items: center; justify-content: center;
    font-size: 15px; font-weight: 400; letter-spacing: 0.3px;
    line-height: 1;
    margin-top: 6px;
  }
  .person-title::before, .person-title::after {
    content: ""; width: 82px; height: 1px; background: var(--white);
    margin: 0 7px;
  }
  .address { font-size: 14px; line-height: 1; margin-top: 13px; }
  .lines { font-size: 14px; line-height: 1; margin-top: 5px; }
  .lines .label { color: var(--gold); }

  .web-band {
    position: absolute; left: 0; top: 309px;
    width: 100%; height: 34px;
    background: linear-gradient(90deg, var(--gold-deep), var(--gold-light) 50%, var(--gold-deep));
    text-align: center;
    font-size: 14px; letter-spacing: 2px;
    line-height: 34px;
    color: var(--ink);
  }

  .social { position: absolute; right: 34px; top: 36px; display: flex; gap: 3px; }
  .social-dot { width: 27px; height: 27px; border-radius: 50%; background: var(--ink); }

  .back-web {
    position: absolute; left: 0; width: 100%; top: 282px;
    text-align: center;
    font-size: 14.5px; letter-spacing: 4px;
    color: var(--ink);
  }
</style>
</head>
<body>

  <section class="card card-front">
    <div class="brand">
      <div class="brand-mark"></div>
      <div class="brand-text">
        <div class="brand-name">DRELVANE</div>
        <div class="brand-division">PINECREST HAULERS DIVISION</div>
      </div>
    </div>

    <div class="contact-band">
      <div class="person-name">TODD MARLOW</div>
      <div class="person-title">CHIEF EXECUTIVE</div>
      <div class="address">1420 Cedar Mill Road, Marietta, Georgia 30060</div>
      <div class="lines">
        <span class="label">P:</span> 404 555 0162
        <span class="label">M:</span> 404 555 0147
        <span class="label">E:</span> todd@Pinecresthaulers-demo.com
      </div>
    </div>

    <div class="web-band">www.Pinecresthaulers-demo.com</div>
  </section>

  <section class="card card-back">
    <div class="social" aria-label="Social media links">
      <span class="social-dot"></span>
      <span class="social-dot"></span>
    </div>

    <div class="brand">
      <div class="brand-mark"></div>
      <div class="brand-text">
        <div class="brand-name">DRELVANE</div>
        <div class="brand-division">PINECREST HAULERS DIVISION</div>
      </div>
    </div>

    <div class="back-web">www.Pinecresthaulers-demo.com</div>
  </section>

</body>
</html>
```